Wordpress Design Project

Hello Happy People,

My name is Tav i run a company called brightpath.net.au am working on a new project with LED lighting and have decided to try pixel guild as i've heard great things.

Our company is in need of wordpress design for a new company 'glow arc' we are a distribution and sales company dealing with the best LED lighting products in the world :)

We are targeting commercial customers, small and medium also!

I would like a wordpress design based on the logos, pictures and content that i provide.

home page
distributor
lighting school
small medium enterprise
commercial enterprise
industrial and mining
product categories (30 products)
contact us

We will be on workmesh & chatterly

Our company website is www.glowarc.com.au and www.vexor.com.au

I am available for the next 10 days to go through with anyone that is interested in taking this project on and will offer work

Industry/Entity Type

School

Requirements
Must have
• i would like the website to follow the design logo i have created originally

```html
<!DOCTYPE html>
<html lang="en">
<head>
<meta charset="utf-8">
<title>Glow Arc – LED Lighting</title>
<link href="https://fonts.googleapis.com/css2?family=PT+Sans:wght@400;700&family=PT+Sans+Narrow&family=Noto+Sans:wght@400;700&display=swap" rel="stylesheet">
<style>
:root{
  --amber:#f3b51c;
  --amber-deep:#dc9a08;
  --ink:#4d4a45;
  --text:#222;
  --footer:#57534e;
  --footer-base:#2c2a27;
  --footer-text:#e8e6e2;
  --field:#67635d;
  --white:#fff;
}
*{box-sizing:border-box;margin:0;padding:0}
html,body{width:1200px;height:1162px;overflow:hidden}
body{font-family:"Noto Sans",sans-serif;color:var(--text);background:var(--white);position:relative}
.header{height:115px;background:linear-gradient(#e9eff5,#fff 70%);position:relative}
.brand{position:absolute;left:186px;top:26px;display:flex;align-items:center;gap:12px}
.brand-dot{width:50px;height:50px;border-radius:50%;background:var(--amber)}
.brand-name{font-family:"PT Sans",sans-serif;font-weight:700;font-size:46px;color:var(--ink);letter-spacing:-1px}
.social{position:absolute;right:200px;top:18px;display:flex;gap:10px}
.social span{font-family:"PT Sans",sans-serif;font-size:13px;color:var(--ink);display:flex;align-items:center;gap:5px}
.social i{display:inline-block;width:14px;height:14px;background:var(--ink);border-radius:3px}
.nav{position:absolute;top:115px;left:0;width:1200px;height:35px;background:var(--amber);border-bottom:1px solid #fff;display:flex;align-items:center;padding-left:190px;gap:16px}
.nav a{font-family:"PT Sans Narrow",sans-serif;color:#fff;font-size:14px;text-decoration:none;text-transform:uppercase;white-space:nowrap}
.nav svg{margin-right:4px}
.hero{position:absolute;top:150px;left:0;width:1200px;height:331px;background:var(--amber)}
.hero-photo{position:absolute;left:178px;top:0;width:844px;height:331px;background:linear-gradient(#2a4fa3 0%,#7d93c4 35%,#e7c79a 55%,#6b5a43 75%,#3b4a2c 100%)}
.hero-arrow{position:absolute;top:132px}
.pager{position:absolute;bottom:6px;display:flex;gap:6px}
.pager span{width:13px;height:13px;border:1px solid #fff;background:#444;color:#fff;font-size:9px;line-height:11px;text-align:center}
.pager span.on{background:#fff;color:#222}
.main{position:absolute;top:481px;left:0;width:1200px;height:431px;background:linear-gradient(#c9c9c9,#fff 80px)}
.welcome{position:absolute;left:194px;top:32px;width:591px}
.welcome h1,.featured h2{font-family:"PT Sans",sans-serif;font-weight:400;color:#4a4a4a}
.welcome h1{font-size:27px;margin-bottom:8px}
.welcome p{font-size:11.2px;line-height:17.8px;text-align:justify;text-align-last:justify;letter-spacing:.2px;height:125px;overflow:hidden}
.featured{position:absolute;left:193px;top:225px}
.featured h2{font-size:22px;margin-bottom:10px}
.product-strip{width:591px;height:160px;background:var(--amber);border:2px solid #f7d98a;border-radius:4px;padding:8px;display:flex;gap:9px}
.product{width:137px;height:140px;background:#fff;border:2px solid #f9e2a4;display:flex;flex-direction:column;align-items:center;padding-top:6px}
.product-photo{width:120px;height:100px;background:radial-gradient(#f2f2f2,#9a9a9a)}
.product span{font-family:"PT Sans",sans-serif;font-weight:700;font-size:18px;color:#555;white-space:nowrap}
.sidebar{position:absolute;left:804px;top:71px;width:204px;height:350px;background:linear-gradient(90deg,var(--amber-deep),var(--amber));border:2px solid #f7dfa3;border-radius:5px;padding:3px}
.sidebar-photo{height:88px;background:linear-gradient(#fff,#b9b9b9)}
.sidebar ul{list-style:none}
.sidebar li{height:48px;border-bottom:1px solid #f6cf6c;display:flex;align-items:center;gap:3px;padding-left:2px;font-family:"PT Sans",sans-serif;font-weight:700;font-size:15.5px;letter-spacing:-.2px;color:#fff;white-space:nowrap}
.sidebar li:last-child{border:none}
.footer{position:absolute;top:912px;left:0;width:1200px;height:213px;background:var(--footer);color:var(--footer-text)}
.footer h3{font-family:"PT Sans",sans-serif;font-weight:400;font-size:17px;margin-bottom:12px}
.sitemap{position:absolute;left:191px;top:10px}
.sitemap a{display:block;font-size:11.5px;color:var(--footer-text);text-decoration:none;letter-spacing:.5px;line-height:20.5px}
.quick{position:absolute;left:487px;top:10px;width:224px}
.quick .field{height:22px;border:1px solid #aaa5a0;border-radius:3px;background:var(--field);font-size:11px;padding:3px 6px;margin-bottom:6px}
.quick .field.msg{height:45px}
.quick .btn{margin:10px 0 0 32px;width:157px;height:30px;border-radius:3px;background:linear-gradient(#222,#888 50%,#222);font-family:"PT Sans",sans-serif;font-weight:700;font-size:15px;color:#fff;text-align:center;line-height:30px}
.contact{position:absolute;left:829px;top:10px;font-size:11.5px;line-height:18px;letter-spacing:.3px}
.contact strong{display:block;font-weight:700;font-size:13.5px;margin:4px 0 8px}
.base{position:absolute;top:1125px;left:0;width:1200px;height:37px;background:var(--footer-base);border-top:1px solid #888;color:#ccc;font-family:"PT Sans",sans-serif;font-size:10.5px;text-align:center;line-height:36px}
</style>
</head>
<body>
<header class="header">
  <div class="brand"><span class="brand-dot"></span><span class="brand-name">Glow Arc</span></div>
  <div class="social"><span><i></i>chatterly</span><span><i></i>workmesh</span></div>
</header>
<nav class="nav">
  <svg width="28" height="24" viewBox="0 0 28 24"><path d="M14 2 2 13h4v10h16V13h4z" fill="#fff"/></svg>
  <a href="#">Distributor</a><a href="#">Lighting School</a><a href="#">Small Medium Enterprise</a><a href="#">Commercial Enterprise</a><a href="#">Industrial and Mining</a><a href="#">Product</a><a href="#">Contact Us</a>
</nav>
<section class="hero">
  <div class="hero-photo" role="img" aria-label="Dusk photograph of a lit suburban house with palm trees and a paved driveway"></div>
  <svg class="hero-arrow" style="left:180px" width="30" height="40" viewBox="0 0 30 40"><path d="M24 3 6 20l18 17" stroke="#fff" stroke-width="7" fill="none"/></svg>
  <svg class="hero-arrow" style="left:990px" width="30" height="40" viewBox="0 0 30 40"><path d="M6 3l18 17L6 37" stroke="#fff" stroke-width="7" fill="none"/></svg>
  <div class="pager" style="left:566px"><span>1</span><span class="on">2</span><span>3</span><span>4</span></div>
</section>
<main class="main">
  <section class="welcome">
    <h1>Welcome to Glow Arc</h1>
    <p>This is Pixelcraft's version of Lorem Ipsum. Proin gravida nibh vel velit auctor aliquet. Aenean sollicitudin, lorem quis bibendum auctor, nisi elit consequat ipsum, nec sagittis sem nibh id elit. Duis sed odio sit amet nibh vulputate cursus a sit amet mauris. Morbi accumsan ipsum velit. Nam nec tellus a odio tincidunt auctor a ornare odio. Sed non mauris vitae erat consequat auctor eu in elit. Class aptent taciti sociosqu ad litora torquent per conubia nostra, per inceptos himenaeos. Mauris in erat justo. Nullam ac urna eu felis dapibus condimentum sit amet a augue. Sed non neque elit. Sed ut imperdiet nisi. Proin condimentum fermentum nunc. Etiam pharetra, erat sed fermentum feugiat, velit mauris egestas quam, ut aliquam</p>
  </section>
  <section class="featured">
    <h2>Feauture Products</h2>
    <div class="product-strip">
      <div class="product"><div class="product-photo" role="img" aria-label="LED downlight"></div><span>Products 1</span></div>
      <div class="product"><div class="product-photo" role="img" aria-label="White LED downlight"></div><span>Products 2</span></div>
      <div class="product"><div class="product-photo" role="img" aria-label="LED bulb with multiple diodes"></div><span>Products 3</span></div>
      <div class="product"><div class="product-photo" role="img" aria-label="LED reflector lamp"></div><span>Products 4</span></div>
    </div>
  </section>
  <aside class="sidebar">
    <div class="sidebar-photo" role="img" aria-label="Close-up of LED lamps"></div>
    <ul>
      <li><svg width="12" height="14"><path d="M3 2l6 5-6 5" stroke="#fff" stroke-width="3" fill="none"/></svg>Distributor</li>
      <li><svg width="12" height="14"><path d="M3 2l6 5-6 5" stroke="#fff" stroke-width="3" fill="none"/></svg>Lighting School</li>
      <li><svg width="12" height="14"><path d="M3 2l6 5-6 5" stroke="#fff" stroke-width="3" fill="none"/></svg>Small Medium Enterprise</li>
      <li><svg width="12" height="14"><path d="M3 2l6 5-6 5" stroke="#fff" stroke-width="3" fill="none"/></svg>Commercial Enterprise</li>
      <li><svg width="12" height="14"><path d="M3 2l6 5-6 5" stroke="#fff" stroke-width="3" fill="none"/></svg>Industrial and Mining</li>
    </ul>
  </aside>
</main>
<footer class="footer">
  <div class="sitemap">
    <h3>Sitemap</h3>
    <a href="#">Home</a><a href="#">Distributor</a><a href="#">Lighting School</a><a href="#">Small Medium Enterprise</a><a href="#">Commercial Enterprise</a><a href="#">Industrial and Mining</a><a href="#">Product</a><a href="#">Contact Us</a>
  </div>
  <div class="quick">
    <h3>Quick Contact</h3>
    <div class="field">Name:</div>
    <div class="field">E-mail:</div>
    <div class="field msg">Message:</div>
    <div class="btn">Subscribe</div>
  </div>
  <div class="contact">
    <h3>Contact Info</h3>
    <strong>Glow Arc</strong>
    Office Phone +61 8 5550 1420<br>Mobile +61 400 555 219<br>42 Harbour Lane,<br>Elmstead, 5190 SA
  </div>
</footer>
<div class="base">Copyright 2012 Glow Arc. All rights reserved.</div>
</body>
</html>
```